Nutrivo, site for appointments between nutritionists and patients

Nutrivo is a platform for connecting nutritionists and patients with appointment scheduling and online payment.

We like teal, but we're not fixated on it.

The site must be simple, accessible and pleasant and dynamic and evoke the joy of nutrition while not forgetting the health aspect.

Example of illustration which tend towards what we are looking for.

Logo and graphic charter

Home page, simple little information

1)
Book a physical or video consultation with a dietitian (medirova, so calm now, léna, vistam)

2)
Reason for using Nutrivo

Access state-certified nutrition experts with several years of training (registration of professionals on the site only with adeli number and valid diploma)

Access the availability of tens of thousands of healthcare professionals.

Make an appointment online, 24/7, for a physical or video consultation.

Secure personal data

3)
You are a dietitian nutritionist

Use nutrivo to optimize your activity
Free up time by making an appointment online
Limit unfulfilled appointments with online payment
Take advantage of Nutrivo's notoriety to obtain better visibility
Use a commercial platform to develop your patient base
Use the platform's communication tools
Etc ...

Page 2 if applicable

List of professionals

Page 3 if search by specific name

Name photo
The essentials, map and access information, presentation, timetables, prices, site, make an appointment

Page 3 bis more in-depth presentation.

Page 4
agenda appointment booking page

Payment page

Professional page

Page 1
presentation of assets

Page 2 limited access

Rates with bronze, silver, gold, platinum account

Products, training and services page for sale

Blog page

Nutrivo is a platform that connects nutritionists and patients with online appointments and payment.

We like the teal color but we are not set on it.

The site must be simple, accessible, pleasant and dynamic and evoke the joy of nutrition while not forgetting the health aspect.

Example of illustrations that tend towards what we are looking for.

Our Logo is on the attachment

Home page

1)
Book a physical or video consultation with a dietician (ex site: medirova, so calm now, léna, vistam)

2)
Reasons to use Nutrivo

Access to experts in nutrition with several years of training (registration of professionals on the site only with adeli number and valid diploma)

Access the availability of tens of thousands of dieticians.

Secure personal data

3) You are a dietitian nutritionist

Free up time with online appointment booking
Limit the number of missed appointments thanks to online payment
Take advantage of Nutrivo's notoriety to get a better visibility
Use the communication tools of the platform
Etc ...

Page 2 if the patient don't choose a professional and put only a place.

List of professionals

Page 3 if searching by specific name

Photo name
The essentials, map and access information, presentation, opening hours, rates, site, make an appointment

Page 3 bis - more detailed presentation of dietician.

Page 4
diary page for making an appointment

Payment page

Blog page

Side Professional page

Page 1
presentation of assets

Page 2 (limited access)

Page 3

Products, training and services for sale page

Target Market(s)

The general public

Number of Pages Required

5+ page

Colors
00AB8E
00BBA5
67D7C9
C6EFE9
E9F9F6

Requirements
Must have
• Read the project in the attached documents. Read the project on the attachments
Should not have
• No photographs

```html
<!DOCTYPE html>
<html lang="en">
<head>
<meta charset="utf-8">
<title>Nutrivo — Your Personal Nutritionist</title>
<link rel="stylesheet" href="https://fonts.googleapis.com/css2?family=Roboto:wght@400;500;700;900&family=Parisienne&display=swap">
<style>
:root{
  --teal:#00BBA5;
  --teal-dark:#00AB8E;
  --teal-mid:#67D7C9;
  --teal-soft:#C6EFE9;
  --teal-pale:#E9F9F6;
  --ink:#111111;
  --text:#2b2b2b;
  --gray:#ececec;
  --white:#ffffff;
}
*{margin:0;padding:0;box-sizing:border-box}
html,body{width:1200px;height:4392px;overflow:hidden}
body{font-family:'Roboto',sans-serif;color:var(--text);background:var(--white);position:relative}
.abs{position:absolute}
.btn{position:absolute;display:flex;align-items:center;justify-content:center;background:var(--teal);color:var(--white);font-weight:700;font-size:16px;text-decoration:none;border-radius:2px}
.script{position:absolute;left:0;width:1200px;text-align:center;font-family:'Parisienne',cursive;color:var(--teal);font-size:36px}
.section-title{position:absolute;left:0;width:1200px;text-align:center;font-weight:700;font-size:46px;color:var(--ink)}
.photo{position:absolute}

/* header */
.site-header{position:absolute;top:0;left:0;width:1200px;height:89px;background:var(--white);border-top:5px solid var(--teal);box-shadow:0 2px 6px rgba(0,0,0,.06);z-index:2}
.brand{position:absolute;left:20px;top:18px;display:flex;align-items:center;gap:8px}
.brand-dot{width:34px;height:34px;border-radius:50%;background:var(--teal-dark)}
.brand-name{font-weight:700;font-size:24px;color:var(--teal-dark)}
.nav a{position:absolute;top:34px;font-size:15px;font-weight:500;color:var(--ink);text-decoration:none}
.nav a.active{color:var(--teal)}
.btn-appoint{left:873px;top:29px;width:197px;height:34px;font-size:16px;letter-spacing:.3px}

/* hero */
.hero{position:absolute;top:89px;left:0;width:1200px;height:569px;background:linear-gradient(100deg,#f1f0ee 0%,#ebe9e6 42%,#d9c9b4 62%,#b9874f 78%,#c6d9a0 100%)}
.hero-title{position:absolute;left:37px;top:128px;font-size:62px;line-height:70px;font-weight:900;color:var(--teal)}
.hero-text{position:absolute;left:37px;top:289px;width:540px;font-size:14px;line-height:26px;color:var(--ink)}
.slider-dots{position:absolute;left:1084px;top:543px;display:flex;gap:6px}
.slider-dots span{width:24px;height:6px;border:2px solid var(--teal);border-radius:2px}

/* feature band */
.features{position:absolute;top:658px;left:0;width:1200px;height:176px;background:var(--teal)}
.feature{position:absolute;top:30px;width:220px;text-align:center;color:var(--white);font-weight:700;font-size:17px}
.feature svg{display:block;margin:0 auto 10px;height:80px}

/* services */
.service-img{position:absolute;border:6px solid #f2f2f2;border-radius:8px;box-shadow:0 2px 6px rgba(0,0,0,.15)}
.service-title{position:absolute;text-align:center;font-size:22px;font-weight:500;color:var(--teal)}
.service-text{position:absolute;text-align:center;font-size:14px;line-height:26px;color:var(--ink)}

/* about */
.about{position:absolute;top:1420px;left:0;width:1200px;height:532px}
.about-bg{position:absolute;inset:0}
.about h2{position:absolute;left:20px;top:66px;font-size:40px;line-height:53px;font-weight:500;color:var(--ink)}
.about h2 em{font-style:normal;color:var(--teal)}
.about p{position:absolute;left:20px;top:192px;width:540px;font-size:14px;line-height:26px;color:var(--ink)}
.contact-row{position:absolute;left:20px;display:flex;align-items:center;gap:40px;font-size:16px;font-weight:500;color:var(--ink)}
.video{position:absolute;left:595px;top:116px;width:585px;height:390px;border-radius:6px;background:linear-gradient(135deg,#d6d4cf 0%,#eceae6 40%,#e9d6c8 60%,#9db36a 85%,#e2a43c 100%)}
.play{position:absolute;left:250px;top:166px;width:86px;height:58px;border-radius:14px;background:var(--white);display:flex;align-items:center;justify-content:center}

/* articles */
.post-title{position:absolute;font-weight:500;color:var(--ink)}
.post-text{position:absolute;font-size:14px;line-height:26px;color:var(--ink)}
.post-meta{position:absolute;font-size:12px;color:var(--ink);word-spacing:2px}
.post-meta span{margin-left:22px}
.side-post .post-title{font-size:20px;line-height:28px;width:290px}
.side-post .post-text{font-size:13px;line-height:26px;width:290px}
.side-post .post-meta{font-size:11px}

/* pricing */
.pricing{position:absolute;top:2804px;left:0;width:1200px;height:525px;background:var(--teal)}
.pricing h2{position:absolute;left:53px;top:30px;font-size:37px;line-height:43px;font-weight:700;color:var(--ink)}
.pricing h2 .light{color:var(--white)}
.pricing p{position:absolute;left:53px;top:168px;width:400px;font-size:13px;line-height:26px;color:var(--white)}
.btn-outline{position:absolute;left:56px;top:268px;width:172px;height:47px;border:3px solid var(--white);color:var(--white);font-weight:700;font-size:16px;display:flex;align-items:center;justify-content:center}
.plan{position:absolute;top:44px;width:285px;height:437px;background:var(--white);border-radius:10px;text-align:center}
.plan h3{margin-top:40px;font-size:22px;font-weight:500;color:var(--teal)}
.plan .price{margin-top:22px;font-size:68px;font-weight:700;color:var(--ink);line-height:74px}
.plan .price sup{font-size:38px;vertical-align:-6px;margin-right:4px}
.plan ul{list-style:none;margin-top:20px;font-size:16px;line-height:35px;color:var(--ink)}
.plan .btn{left:55px;top:353px;width:175px;height:46px}

/* testimonials */
.quote-box{position:absolute;left:252px;top:3516px;width:696px;height:384px;border:9px solid var(--teal);border-radius:10px;text-align:center}
.quote-box p{margin:45px auto 0;width:600px;font-size:17px;line-height:30px;color:var(--ink)}
.avatar{width:132px;height:132px;border-radius:50%;margin:30px auto 0;background:radial-gradient(circle at 50% 40%,#3b4a5c,#1b2430)}
.quote-name{margin-top:12px;font-size:20px;font-weight:700;color:var(--teal)}

/* footer */
.footer{position:absolute;top:3971px;left:0;width:1200px;height:421px}
.footer-brand{position:absolute;left:130px;top:160px;display:flex;align-items:center;gap:8px}
.footer-about{position:absolute;left:20px;top:252px;width:360px;text-align:center;font-size:14px;line-height:30px;color:var(--ink)}
.footer-col{position:absolute;top:222px;font-size:16px;line-height:30px;color:var(--ink)}
.newsletter-title{position:absolute;left:787px;top:222px;font-size:16px;color:var(--ink)}
.newsletter-input{position:absolute;left:787px;top:258px;width:309px;height:43px;background:var(--white);border:1px solid #ddd;padding-left:16px;display:flex;align-items:center;font-size:15px;color:var(--teal)}
.newsletter-btn{position:absolute;left:1101px;top:258px;width:63px;height:43px;border:3px solid var(--teal);background:var(--white);display:flex;align-items:center;justify-content:center}
.footer-line{position:absolute;left:20px;top:377px;width:1160px;height:2px;background:var(--teal)}
.copyright{position:absolute;left:0;top:386px;width:1200px;text-align:center;font-size:14px;font-weight:500;color:var(--ink)}
</style>
</head>
<body>

<header class="site-header">
  <div class="brand"><span class="brand-dot"></span><span class="brand-name">nutrivo</span></div>
  <nav class="nav">
    <a class="active" style="left:406px">Home</a>
    <a style="left:487px">About us</a>
    <a style="left:590px">Products</a>
    <a style="left:694px">Blog</a>
    <a style="left:765px">Contacts</a>
  </nav>
  <a class="btn btn-appoint">APPOINTMENTS</a>
</header>

<section class="hero" role="img" aria-label="Hands holding a heart-shaped bowl of fresh fruit and vegetables with a stethoscope">
  <h1 class="hero-title">Your Personal<br>Nutritionist</h1>
  <p class="hero-text">Lorem Ipsum is simply dummy text of the printing and typesetting industry. Lorem Ipsum has been the industry's standard dummy text ever printer took a galley of type and scrambled it to make a type specimen book.</p>
  <a class="btn" style="left:37px;top:409px;width:178px;height:49px">Read More</a>
  <a class="btn" style="left:261px;top:409px;width:177px;height:49px">View Plans</a>
  <div class="slider-dots"><span></span><span></span><span></span></div>
</section>

<section class="features">
  <div class="feature" style="left:43px">
    <svg viewBox="0 0 90 80" width="90"><path d="M45 76 C10 50 2 36 2 22 A20 20 0 0 1 45 14 A20 20 0 0 1 88 22 C88 36 80 50 45 76Z" fill="#fff"/><polyline points="12,40 32,40 38,28 46,54 52,34 58,40 78,40" fill="none" stroke="#00BBA5" stroke-width="4" stroke-linejoin="round"/></svg>
    Health Improving</div>
  <div class="feature" style="left:355px">
    <svg viewBox="0 0 70 80" width="70"><path d="M35 24 C20 14 4 20 4 42 C4 62 18 78 30 78 C33 78 35 76 35 76 C35 76 37 78 40 78 C52 78 66 62 66 42 C66 20 50 14 35 24Z" fill="#fff"/><path d="M35 24 C35 16 38 8 44 4" stroke="#fff" stroke-width="4" fill="none"/><path d="M38 14 C46 4 58 6 60 10 C52 16 44 16 38 14Z" fill="#fff"/></svg>
    Diet Strategies</div>
  <div class="feature" style="left:660px">
    <svg viewBox="0 0 80 80" width="80"><path d="M8 74 C2 56 6 40 18 34 C28 28 38 36 44 30 C48 26 40 18 44 10 C50 2 64 4 70 12 C78 24 78 48 70 62 C62 74 40 78 8 74Z" fill="#fff"/></svg>
    Workout Plans</div>
  <div class="feature" style="left:957px">
    <svg viewBox="0 0 80 80" width="80"><path d="M24 6 C28 20 26 34 22 44 C18 56 22 70 30 76 L50 76 C58 70 62 56 58 44 C54 34 52 20 56 6Z" fill="#fff"/><path d="M4 22 H18 M12 16 L18 22 L12 28 M76 22 H62 M68 16 L62 22 L68 28" stroke="#fff" stroke-width="3" fill="none"/><path d="M30 50 Q40 62 50 50" stroke="#00BBA5" stroke-width="3" fill="none"/></svg>
    Weight Loss</div>
</section>

<section class="services">
  <div class="script" style="top:895px">My services</div>
  <h2 class="section-title" style="top:938px">Let's change your life</h2>

  <div class="photo service-img" style="left:41px;top:1058px;width:308px;height:200px;background:linear-gradient(135deg,#c9d7e6,#8ea9c8 50%,#d7b28e)" role="img" aria-label="Group of people raising hands together"></div>
  <div class="service-title" style="left:20px;top:1268px;width:352px">Life Motivation</div>
  <div class="service-text" style="left:20px;top:1305px;width:352px">Lorem Ipsum is simply dummy text of the printing and typesetting industry. Lorem Ipsum has been the industry's standard dummy</div>

  <div class="service-title" style="left:415px;top:1053px;width:370px">Nutrition Programs</div>
  <div class="service-text" style="left:415px;top:1091px;width:370px">Lorem Ipsum is simply dummy text of the printing and typesetting industry. Lorem Ipsum has been the industry's standard dummy</div>
  <div class="photo service-img" style="left:447px;top:1183px;width:305px;height:194px;background:linear-gradient(135deg,#e8edf0,#c7d3da 50%,#e6c69a)" role="img" aria-label="Nutritionist consulting with a patient at a desk"></div>

  <div class="photo service-img" style="left:851px;top:1058px;width:306px;height:200px;background:linear-gradient(135deg,#9bc07a,#6f9a4e 50%,#c9b59d)" role="img" aria-label="Man exercising outdoors"></div>
  <div class="service-title" style="left:828px;top:1268px;width:352px">Fitness Trainigns</div>
  <div class="service-text" style="left:828px;top:1305px;width:352px">Lorem Ipsum is simply dummy text of the printing and typesetting industry. Lorem Ipsum has been the industry's standard dummy</div>
</section>

<section class="about">
  <svg class="about-bg" width="1200" height="532" viewBox="0 0 1200 532"><path d="M0 30 Q700 48 1200 0 V532 H0Z" fill="#ececec"/></svg>
  <h2>Hello, I’m <em>Alex Greenfield</em> —<br>your personal nutritionist</h2>
  <p>Lorem Ipsum is simply dummy text of the printing and typesetting industry. Lorem Ipsum has been the industry's standard dummy text ever printer took a galley of type and scrambled it to make a type specimen book.</p>
  <div class="contact-row" style="top:298px">
    <svg width="46" height="44" viewBox="0 0 46 44"><circle cx="23" cy="22" r="19" fill="none" stroke="#00BBA5" stroke-width="4" stroke-dasharray="90 12"/><path d="M23 10 V22 L31 28" stroke="#00BBA5" stroke-width="4" fill="none"/></svg>
    <span>24/7, for a physical or video consultation.</span></div>
  <div class="contact-row" style="top:368px">
    <svg width="46" height="40" viewBox="0 0 46 40"><path d="M3 14 C3 4 43 4 43 14 L43 18 L33 18 L33 12 L13 12 L13 18 L3 18Z" fill="#00BBA5"/><path d="M10 22 H36 L40 38 H6Z" fill="#00BBA5"/><circle cx="23" cy="29" r="5" fill="#ececec"/></svg>
    <span>+30-6900112233</span></div>
  <a class="btn" style="left:20px;top:460px;width:178px;height:48px">Read More</a>
  <div class="video" role="img" aria-label="Smiling nutritionist holding an apple in her office">
    <div class="play"><svg width="30" height="32" viewBox="0 0 30 32"><path d="M2 2 L28 16 L2 30Z" fill="#00BBA5"/></svg></div>
  </div>
</section>

<section class="articles">
  <div class="script" style="top:2012px">Top posts</div>
  <h2 class="section-title" style="top:2057px">Recent articles</h2>

  <div class="photo" style="left:46px;top:2143px;width:576px;height:405px;background:linear-gradient(120deg,#eef0f0,#dfe4e6 45%,#a9c46a 75%,#e58a3a)" role="img" aria-label="Nutritionist at a desk with fresh vegetables"></div>
  <div class="post-title" style="left:46px;top:2555px;font-size:27px">How many calories an adult needs per day</div>
  <div class="post-text" style="left:46px;top:2593px;width:530px">Lorem Ipsum is simply dummy text of the printing and typesetting industry. Lorem Ipsum has been the industry's standard dummy text ever printer took a galley Lorem Ipsum is simply dummy text of the printing and typesetting industry. Lorem Ipsum has been the industry's standard</div>
  <div class="post-meta" style="left:46px;top:2722px;font-size:13px">November 2, 2021<span>0 comments</span></div>

  <div class="side-post">
    <div class="photo" style="left:658px;top:2143px;width:222px;height:126px;background:linear-gradient(120deg,#6d4a32,#c9a47c 50%,#8fb657)" role="img" aria-label="Woman preparing healthy food"></div>
    <div class="post-title" style="left:891px;top:2139px">How many calories an adult needs per day</div>
    <div class="post-text" style="left:891px;top:2197px">Lorem Ipsum is simply dummy text of the printing and typesetting industry.</div>
    <div class="post-meta" style="left:891px;top:2254px">November 2, 2021<span>0 comments</span></div>

    <div class="photo" style="left:658px;top:2316px;width:222px;height:127px;background:linear-gradient(120deg,#eeeeee,#c9a07a 45%,#e25a3a 65%,#8ec14d)" role="img" aria-label="Heart-shaped bowl of fruit with stethoscope"></div>
    <div class="post-title" style="left:891px;top:2313px">How many calories an adult needs per day</div>
    <div class="post-text" style="left:891px;top:2371px">Lorem Ipsum is simply dummy text of the printing and typesetting industry.</div>
    <div class="post-meta" style="left:891px;top:2428px">November 2, 2021<span>0 comments</span></div>

    <div class="photo" style="left:658px;top:2490px;width:222px;height:126px;background:linear-gradient(120deg,#e9b44c,#f1ece4 45%,#9ec25a 70%,#d8493a)" role="img" aria-label="Diet plan on a tablet beside fresh produce"></div>
    <div class="post-title" style="left:891px;top:2487px">How many calories an adult needs per day</div>
    <div class="post-text" style="left:891px;top:2545px">Lorem Ipsum is simply dummy text of the printing and typesetting industry.</div>
    <div class="post-meta" style="left:891px;top:2602px">November 2, 2021<span>0 comments</span></div>
  </div>
  <a class="btn" style="left:977px;top:2688px;width:175px;height:48px">Read More</a>
</section>

<section class="pricing">
  <h2>Choose your program<br>and you will get the<br><span class="light">100% result</span></h2>
  <p>Lorem Ipsum is simply dummy text of the printing and typesetting industry. Lorem Ipsum has been the industry's standard dummy text ever printer took a galley</p>
  <a class="btn-outline">Read More</a>
  <svg class="abs" style="left:247px;top:258px" width="200" height="200" viewBox="0 0 200 200"><circle cx="100" cy="100" r="98" fill="#ffffff"/></svg>

  <div class="plan" style="left:537px">
    <h3>Single consultation</h3>
    <div class="price"><sup>$</sup>19</div>
    <ul><li>1 hour consultation</li><li>Exact calorie content</li><li>Recomendations</li><li>1 week support</li></ul>
    <a class="btn">Read More</a>
  </div>
  <div class="plan" style="left:861px">
    <h3>Nutrition complex</h3>
    <div class="price"><sup>$</sup>35</div>
    <ul><li>Nutrition strategy</li><li>Individual menu</li><li>Improves health</li><li>3 weeks support</li></ul>
    <a class="btn">Read More</a>
  </div>
</section>

<section class="testimonials">
  <div class="script" style="top:3390px">Testimonials</div>
  <h2 class="section-title" style="top:3435px">What our Clients Say</h2>
  <svg class="abs" style="left:190px;top:3690px" width="26" height="40" viewBox="0 0 26 40"><polyline points="22,4 6,20 22,36" fill="none" stroke="#00BBA5" stroke-width="5"/></svg>
  <svg class="abs" style="left:986px;top:3690px" width="26" height="40" viewBox="0 0 26 40"><polyline points="4,4 20,20 4,36" fill="none" stroke="#00BBA5" stroke-width="5"/></svg>
  <div class="quote-box">
    <p>Lorem Ipsum is simply dummy text of the printing and typesetting industry. Lorem Ipsum has been the industry's standard dummy text ever since the when an unknown printer took a galley of type and scrambled it to make</p>
    <div class="avatar" role="img" aria-label="Client portrait"></div>
    <div class="quote-name">Marcus</div>
  </div>
</section>

<footer class="footer">
  <svg class="abs" style="left:0;top:0" width="1200" height="421" viewBox="0 0 1200 421"><path d="M0 0 Q600 230 1200 0 V421 H0Z" fill="#ececec"/></svg>
  <div class="footer-brand"><span class="brand-dot" style="width:40px;height:40px"></span><span class="brand-name" style="font-size:30px">nutrivo</span></div>
  <div class="footer-about">Lorem Ipsum is simply dummy text of the printing and typesetting industry. Lorem Ipsum has been the industry's standard dummy text ever since the when an unknown printer took a galley</div>
  <div class="footer-col" style="left:455px">Home<br>About us<br>Products<br>Blog<br>Contacts</div>
  <div class="footer-col" style="left:585px">Phones:<br>+49000-111-22-33<br>+49000-444-55-66</div>
  <div class="newsletter-title">Our Newsletter</div>
  <div class="newsletter-input">Your Email</div>
  <div class="newsletter-btn"><svg width="28" height="26" viewBox="0 0 28 26"><path d="M2 12 L26 2 L20 24 L13 16 Z" fill="#00BBA5"/><path d="M13 16 L26 2" stroke="#fff" stroke-width="2"/></svg></div>
  <div class="footer-line"></div>
  <div class="copyright">© 2021nutrivo, All Rights Reserved</div>
</footer>

</body>
</html>
```